Baby Boutique Needs a Business Card Design

We need a modern double sided business card design using the attached logo for Lil' Tot Nook.

Lil' Tot Nook is a baby boutique which sells only handmade clothing and accessories for both boys and girls. Our store will live exclusively online.

We would like to only use the colors that have been used in the logo.

Target Market(s)

Potential wholesale clients, Small business owners

Industry/Entity Type

Retail

Contact Information for Business Card

Name Wendell J. Ferris (Owner)
Email sales@ltotnook.com
Main Phone 787-203-6159
Cell phone 787-203-6742
Website www.LTotNook.com

Font styles to use
Sans Serif

Colors

Designer to choose colors to be used in the design.

Requirements
Must have
• -Would like to have icons that indentify the contact information.
• -Include our website
• -Include our tagline in a small area near the bottom. "Handmade Baby Creations"
• -Would like to include Facebook and Instagram Icons
• -
Nice to have
• Would like to have a simple back side with the logo.
• Something along the lines of the harbor ledger card attached.

```html
<!DOCTYPE html>
<html lang="en">
<head>
<meta charset="utf-8">
<title>Lil' Tot Nook – Business Card</title>
<link rel="stylesheet" href="https://fonts.googleapis.com/css2?family=Poppins:wght@300;400&display=swap">
<style>
  :root {
    --coral: #dc5d5d;
    --teal: #7ccbbd;
    --ink: #3e3e3e;
    --card: #ffffff;
    --backdrop: #ece8e4;
  }
  * { box-sizing: border-box; margin: 0; padding: 0; }
  html, body { width: 1200px; height: 1090px; overflow: hidden; }
  body {
    background: var(--backdrop);
    font-family: "Poppins", sans-serif;
    position: relative;
  }
  .card {
    position: absolute;
    left: 180px;
    width: 840px;
    height: 480px;
    background: var(--card);
    border-radius: 34px;
    overflow: hidden;
    box-shadow: 0 10px 28px rgba(0,0,0,0.18);
  }
  .card--front { top: 40px; }
  .card--back { top: 570px; }

  .holder { position: absolute; left: 52px; top: 44px; }
  .holder__name {
    font-size: 38px; font-weight: 300; color: var(--coral);
    letter-spacing: 0.5px; padding-left: 34px; line-height: 1.2;
  }
  .holder__meta { display: flex; align-items: flex-end; gap: 4px; margin-top: 2px; }
  .holder__role { font-size: 15px; font-weight: 300; color: var(--ink); line-height: 1; }
  .holder__rule { width: 320px; height: 2px; background: var(--teal); margin-bottom: 1px; }

  .contacts { position: absolute; left: 52px; top: 150px; list-style: none; }
  .contacts li {
    display: flex; align-items: center; gap: 12px;
    font-size: 17px; font-weight: 400; color: var(--ink);
    margin-bottom: 9px;
  }
  .contacts svg { width: 20px; height: 20px; flex: none; }

  .social { position: absolute; left: 40px; top: 302px; display: flex; gap: 10px; }
  .social span {
    width: 30px; height: 30px; border-radius: 50%; background: var(--coral); display: block;
  }

  .band {
    position: absolute; left: 0; right: 0; bottom: 0; height: 110px;
    background: var(--coral);
    border-top: 8px solid var(--teal);
    display: flex; align-items: center; justify-content: center;
  }
  .band__tagline {
    color: #fff; font-weight: 300; font-size: 22px;
    letter-spacing: 3px; text-transform: uppercase;
  }

  .brand { font-weight: 400; color: var(--teal); text-align: center; line-height: 1; white-space: nowrap; }
  .card--front .brand {
    position: absolute; right: 50px; top: 200px; font-size: 42px; width: 280px;
  }
  .card--back .brand {
    position: absolute; left: 0; right: 0; top: 50%; transform: translateY(-50%);
    font-size: 72px;
  }
</style>
</head>
<body>

<section class="card card--front" aria-label="Business card front">
  <div class="holder">
    <p class="holder__name">Wendell J. Ferris</p>
    <div class="holder__meta">
      <p class="holder__role">owner</p>
      <span class="holder__rule"></span>
    </div>
  </div>

  <ul class="contacts">
    <li>
      <svg viewBox="0 0 20 20"><circle cx="10" cy="10" r="10" fill="#7ccbbd"/><path d="M6.5 5.5l2 0 .8 2.4-1.2 1a6 6 0 0 0 3 3l1-1.2 2.4.8 0 2A1.5 1.5 0 0 1 13 15 8.5 8.5 0 0 1 5 7a1.5 1.5 0 0 1 1.5-1.5z" fill="#fff"/></svg>
      787-203-6159
    </li>
    <li>
      <svg viewBox="0 0 20 20"><circle cx="10" cy="10" r="10" fill="#7ccbbd"/><rect x="7" y="4.5" width="6" height="11" rx="1.2" fill="#fff"/><rect x="8" y="6" width="4" height="7" fill="#7ccbbd"/></svg>
      787-203-6742
    </li>
    <li>
      <svg viewBox="0 0 20 20"><circle cx="10" cy="10" r="10" fill="#7ccbbd"/><rect x="5" y="6.5" width="10" height="7" rx="1" fill="#fff"/><path d="M5.5 7l4.5 3.5L14.5 7" fill="none" stroke="#7ccbbd" stroke-width="1"/></svg>
      sales@ltotnook.com
    </li>
    <li>
      <svg viewBox="0 0 20 20"><circle cx="10" cy="10" r="10" fill="#7ccbbd"/><circle cx="10" cy="10" r="5" fill="none" stroke="#fff" stroke-width="1.2"/><path d="M5 10h10M10 5c-2.5 3-2.5 7 0 10M10 5c2.5 3 2.5 7 0 10" fill="none" stroke="#fff" stroke-width="1"/></svg>
      www.LTotNook.com
    </li>
  </ul>

  <div class="social" aria-label="Social media links">
    <span></span><span></span>
  </div>

  <p class="brand">Lil' Tot Nook</p>

  <div class="band">
    <p class="band__tagline">Handmade Baby Creations</p>
  </div>
</section>

<section class="card card--back" aria-label="Business card back">
  <p class="brand">Lil' Tot Nook</p>
</section>

</body>
</html>
```